Cleaning Company and Stayloft Tasks

Our London based company provides services for all things related to Stayloft. Our main tasks are cleaning, checkins & linen. We are in need of a fresh new design that allows customers to book our services with ease.

The site must keep in mind that it will be primarily used on mobile and payment to be taken online.

What we require:

- Two pages designed, Home page (see Homepage doc) and Purchase Page (see flow chart)

Things we like:-

- We like mainly white and pastel based colours.
- Usage of vector style graphics through our the site to represent people & tasks.
- Shopping cart, with lots of images to select services
- Shopping cart that always has the pricing floating on the right
- Shopping cart that is wizard based.
- We like the usage of wonk characters on this site (for us probably angels)
http://www.tradelarks.com/pricing.php
- Slightly quirky design.

Sites we like:
http://vantorigrove.com/ - bold action
https://www.kellimo.com/ - a very playful design

TO AVOID WASTING TIME, INITIALLY DESIGN THE FRONT PAGE ONLY, IF WE LIKE YOUR HOME PAGE DESIGN THEM WE CAN SHORT LIST YOU INTO DESIGNING THE PAYMENT WIZARD PAGE

Target Market(s)

Young working professionals.

Industry/Entity Type

Cleaning Service

Contact Information for Business Card

Name: Rob Parkin
Title: Senior Sales Representative
Tel: +44 (0) 700 9000 0481
Office: +44 (0) 200 946 0718
email: mh@tidyhaven.co.uk
web: www.tidyhaven.co.uk

Number of Pages Required

2 page

Font styles to use
Sans Serif

Colors
876aae
6b449b

Requirements
Must have
• - Two pages designed including home page and wizard to purchase services.
• - Usage of vector images.
Nice to have
• Angels to represent tasks
• We also like the colour yellow, the branding can be changed to suit this colour change.
Should not have
• A design that must not look like a Pagecraft standard Pagecraft theme.

```html
<!DOCTYPE html>
<html lang="en">
<head>
<meta charset="utf-8">
<title>tidyhaven — Book a Local Professional Cleaner</title>
<link rel="stylesheet" href="https://fonts.googleapis.com/css2?family=Oswald:wght@500&family=Roboto:wght@300;400;500&family=Open+Sans:ital,wght@0,400;0,600;1,400&display=swap">
<style>
:root{
  --purple:#6b449b;
  --purple-soft:#876aae;
  --purple-deep:#5a3889;
  --ink:#333;
  --muted:#777;
  --line:#c9bcdc;
  --grey-bg:#f4f4f4;
  --star:#f0b323;
  --white:#fff;
}
*{box-sizing:border-box;margin:0;padding:0}
html,body{width:1200px;height:2880px;overflow:hidden;background:var(--white)}
body{font-family:"Open Sans",Arial,sans-serif;color:var(--ink);position:relative}
.brand{display:flex;align-items:center;gap:12px;font-family:"Roboto",Arial,sans-serif;font-weight:300;color:var(--white);font-size:38px;letter-spacing:.5px}
.brand-dot{width:22px;height:22px;border-radius:50%;background:var(--white)}

/* header */
.site-header{position:absolute;top:0;left:0;width:1200px;height:88px;background:var(--purple);display:flex;align-items:center;justify-content:space-between;padding:0 100px}
.main-nav{display:flex;gap:36px}
.nav-item{display:flex;flex-direction:column;align-items:center;gap:6px;color:var(--white);font-family:"Roboto",Arial,sans-serif;font-weight:500;font-size:13px;letter-spacing:.5px;text-decoration:none}
.nav-item svg{width:14px;height:14px;fill:var(--white)}

/* hero */
.hero{position:absolute;top:88px;left:0;width:1200px;height:552px;background:linear-gradient(110deg,#4d4a4a 0%,#7a6d63 30%,#9a8878 45%,#5d5c61 65%,#8c7f7b 85%,#3e3c40 100%)}
.hero-content{position:absolute;top:210px;left:0;width:100%;text-align:center}
.hero-title{font-family:"Oswald",Arial,sans-serif;font-weight:500;color:var(--white);font-size:48px;line-height:54px;text-transform:uppercase;text-shadow:0 2px 6px rgba(0,0,0,.45)}
.btn-book{display:inline-block;margin-top:26px;padding:0 22px;height:34px;line-height:30px;border:2px solid var(--white);border-radius:18px;background:var(--purple);color:var(--white);font-family:"Roboto",Arial,sans-serif;font-size:15px;text-decoration:none}
.slider-dots{display:flex;justify-content:center;gap:12px;margin-top:20px}
.slider-dots span{width:14px;height:14px;border-radius:50%;border:2px solid rgba(255,255,255,.85)}
.slider-dots span.active{background:var(--purple);border-color:var(--purple-soft)}

/* section heading */
.section-title{display:flex;align-items:center;justify-content:center;gap:12px;font-family:"Roboto",Arial,sans-serif;font-weight:400;color:var(--purple);font-size:34px}
.section-title .mark{width:18px;height:18px;border-radius:50%;background:var(--purple)}
.rule{width:72px;height:1px;background:var(--purple-soft);margin:22px auto 0}

/* services */
.services{position:absolute;top:640px;left:0;width:1200px;height:458px}
.services .section-title{margin-top:76px}
.service-list{position:absolute;top:204px;left:0;width:100%;display:flex;justify-content:center;gap:49px;list-style:none}
.service{width:210px;text-align:center}
.service svg{width:72px;height:72px;stroke:#777;fill:none;stroke-width:2}
.service h3{font-family:"Roboto",Arial,sans-serif;font-weight:400;font-size:17px;color:var(--ink);margin-top:16px}
.service p{font-size:11.5px;line-height:20px;color:var(--muted);margin-top:12px}

/* why us */
.why{position:absolute;top:1098px;left:0;width:1200px;height:528px;display:flex}
.why-photo{width:582px;height:100%;background:linear-gradient(140deg,#8a9a4a 0%,#5e7a2e 35%,#c2b469 60%,#40602a 100%)}
.why-panel{flex:1;background:radial-gradient(circle at 80% 30%,#7b58a9 0%,var(--purple) 55%,var(--purple-deep) 100%);padding:80px 0 0 68px;color:var(--white)}
.why-panel .section-title{justify-content:flex-start;color:var(--white)}
.why-panel .section-title .mark{background:var(--white)}
.why-list{list-style:none;margin-top:24px}
.why-item{display:flex;align-items:flex-start;gap:22px;margin-bottom:22px}
.why-icon{width:66px;height:66px;flex:none;border-radius:50%;border:2px solid rgba(255,255,255,.55);display:flex;align-items:center;justify-content:center}
.why-icon svg{width:28px;height:28px;stroke:var(--white);fill:none;stroke-width:2}
.why-item h3{font-family:"Roboto",Arial,sans-serif;font-weight:400;font-size:17px;margin-top:2px}
.why-item p{font-size:11.5px;line-height:20px;margin-top:8px;width:380px;opacity:.92}

/* steps */
.steps{position:absolute;top:1626px;left:0;width:1200px;height:508px}
.steps .section-title{margin-top:86px}
.step{position:absolute;top:232px;width:260px;text-align:center}
.step-ring{width:132px;height:132px;margin:0 auto;border-radius:50%;border:2px solid var(--purple-soft);display:flex;align-items:center;justify-content:center}
.step-core{width:112px;height:112px;border-radius:50%;background:var(--purple);display:flex;align-items:center;justify-content:center}
.step-core.soft{background:var(--purple-soft)}
.step-core svg{width:48px;height:48px;stroke:var(--white);fill:none;stroke-width:3}
.step p{font-size:14px;line-height:21px;color:var(--ink);margin-top:20px}
.step-arrow{position:absolute;top:292px;width:90px;height:30px}
.step-arrow svg{width:90px;height:30px;stroke:#e0e0e0;fill:none;stroke-width:5}

/* testimonials */
.testimonials{position:absolute;top:2134px;left:0;width:1200px;height:396px;background:var(--grey-bg);border-top:1px solid #e6e6e6}
.testimonials .section-title{margin-top:56px}
.quote-list{position:absolute;top:164px;left:0;width:100%;list-style:none}
.quote{position:absolute;width:302px;height:190px;background:linear-gradient(#f4f4f4,#fafafa 60%,#f4f4f4);padding:12px 4px 0 8px}
.quote blockquote{font-style:italic;font-size:11.5px;line-height:20px;color:#555;position:relative;padding-left:12px}
.quote blockquote::before{content:"\201C";position:absolute;left:0;top:-6px;font-size:22px;color:#888}
.reviewer{display:flex;align-items:center;gap:22px;margin-top:26px}
.avatar{width:76px;height:76px;border-radius:50%;background:linear-gradient(#d9c3a8,#b39478);border:3px solid var(--white);box-shadow:0 1px 4px rgba(0,0,0,.15)}
.avatar.dark{background:linear-gradient(#8c7b6d,#4d4039)}
.reviewer-name{font-style:italic;font-size:13px;color:var(--purple-soft)}
.stars{color:var(--star);font-size:11px;letter-spacing:1px;margin-top:6px}
.stars .off{color:#ccc}

/* footer */
.site-footer{position:absolute;top:2530px;left:0;width:1200px;height:350px;background:var(--purple);color:var(--white)}
.footer-brand{position:absolute;left:100px;top:92px}
.footer-brand .brand{font-size:32px}
.social{display:flex;gap:18px;margin-top:22px}
.social span{width:24px;height:24px;border-radius:4px;border:2px solid rgba(255,255,255,.85)}
.footer-col{position:absolute;top:48px}
.footer-col h4{font-family:"Roboto",Arial,sans-serif;font-weight:400;font-size:19px;letter-spacing:.3px;text-transform:uppercase}
.footer-col p,.footer-col li{font-size:12px;line-height:22px}
.newsletter{left:378px;width:230px}
.newsletter p{margin-top:14px}
.newsletter .field{margin-top:14px;width:226px;height:42px;background:var(--white);color:#888;font-size:11px;padding:13px 14px}
.newsletter .btn-subscribe{display:inline-block;margin-top:14px;background:#333;color:var(--white);font-size:12px;font-weight:600;padding:11px 16px}
.contact{left:672px;width:240px}
.contact address{font-style:normal;font-size:12px;line-height:22px;margin-top:14px}
.contact-line{display:flex;align-items:center;gap:14px;margin-top:14px;font-size:12px}
.contact-line svg{width:18px;height:18px;stroke:var(--white);fill:none;stroke-width:1.6}
.quick-links{left:964px;width:180px}
.quick-links ul{list-style:none;margin-top:14px}
.quick-links li{position:relative;padding-left:18px}
.quick-links li::before{content:"";position:absolute;left:0;top:8px;border-left:6px solid var(--white);border-top:4px solid transparent;border-bottom:4px solid transparent}
.footer-bar{position:absolute;left:0;top:292px;width:100%;height:58px;border-top:1px solid rgba(255,255,255,.2);font-size:11.5px;text-align:center;line-height:58px;padding-right:40px}
</style>
</head>
<body>

<header class="site-header">
  <div class="brand"><span class="brand-dot"></span>tidyhaven</div>
  <nav class="main-nav">
    <a class="nav-item" href="#"><svg viewBox="0 0 14 14"><circle cx="7" cy="4" r="3.2"/><path d="M1 14c0-4 2.6-6 6-6s6 2 6 6z"/></svg>ABOUT</a>
    <a class="nav-item" href="#"><svg viewBox="0 0 14 14"><circle cx="7" cy="4" r="3.2"/><path d="M1 14c0-4 2.6-6 6-6s6 2 6 6z"/></svg>CONTACT</a>
    <a class="nav-item" href="#"><svg viewBox="0 0 14 14"><path d="M3 6V4a4 4 0 0 1 8 0v2h-2V4a2 2 0 0 0-4 0v2z"/><rect x="2" y="6" width="10" height="8" rx="1"/></svg>LOGIN</a>
  </nav>
</header>

<section class="hero" role="img" aria-label="Photo of a young man with a backpack checking his phone on a city street at dusk">
  <div class="hero-content">
    <h1 class="hero-title">Book a Local<br>Professional Cleaner</h1>
    <a class="btn-book" href="#">Book a Service</a>
    <div class="slider-dots"><span class="active"></span><span></span><span></span></div>
  </div>
</section>

<section class="services">
  <h2 class="section-title"><span class="mark"></span>What We Do</h2>
  <div class="rule"></div>
  <ul class="service-list">
    <li class="service">
      <svg viewBox="0 0 72 72"><rect x="14" y="8" width="38" height="50"/><path d="M22 20h22M22 28h22M22 36h14"/><path d="M36 48l8 8 16-18"/></svg>
      <h3>Stayloft Tasks</h3>
      <p>Sed ut perspiciatis unde omnis iste natus error sit voluptatem accusantium doloremque laudantium.</p>
    </li>
    <li class="service">
      <svg viewBox="0 0 72 72"><circle cx="34" cy="38" r="26"/><circle cx="34" cy="38" r="17"/><circle cx="34" cy="38" r="8"/><path d="M34 38L60 12M52 12h8v8"/></svg>
      <h3>Stayloft Management</h3>
      <p>Sed ut perspiciatis unde omnis iste natus error sit voluptatem accusantium doloremque laudantium.</p>
    </li>
    <li class="service">
      <svg viewBox="0 0 72 72"><path d="M62 6L38 40"/><path d="M38 40l-8-4-22 20c8 6 20 8 30 4l6-12z"/><path d="M18 54l10-10M26 58l8-10"/></svg>
      <h3>Domestic Cleaning</h3>
      <p>Sed ut perspiciatis unde omnis iste natus error sit voluptatem accusantium doloremque laudantium.</p>
    </li>
    <li class="service">
      <svg viewBox="0 0 72 72"><path d="M16 28a20 20 0 0 1 40 0z"/><path d="M10 30h52"/><path d="M36 8v20"/><path d="M20 64l14-14M30 46l10 10M44 44l10-10 8 8-10 10z"/></svg>
      <h3>Handyman</h3>
      <p>Sed ut perspiciatis unde omnis iste natus error sit voluptatem accusantium doloremque laudantium.</p>
    </li>
  </ul>
</section>

<section class="why">
  <div class="why-photo" role="img" aria-label="Photo of hands in yellow and green rubber gloves holding a spray bottle and a cloth"></div>
  <div class="why-panel">
    <h2 class="section-title"><span class="mark"></span>Why Us</h2>
    <ul class="why-list">
      <li class="why-item">
        <div class="why-icon"><svg viewBox="0 0 28 28"><rect x="5" y="6" width="18" height="12" rx="1"/><path d="M2 22h24"/></svg></div>
        <div><h3>Trusted Professionals</h3><p>Our own trusted vetted professionals. They are all experienced, friendly, background checked &amp; insured</p></div>
      </li>
      <li class="why-item">
        <div class="why-icon"><svg viewBox="0 0 28 28"><path d="M5 9a11 11 0 1 1-1 7"/><path d="M3 4v6h6"/><path d="M14 9v6l4 3"/></svg></div>
        <div><h3>Same-day Availability</h3><p>Book online it take a two minutes, and schedule one of our team at your place as early as the same day</p></div>
      </li>
      <li class="why-item">
        <div class="why-icon"><svg viewBox="0 0 28 28"><path d="M14 3l10 4v7c0 6-5 10-10 11C9 24 4 20 4 14V7z"/><path d="M14 3v22"/></svg></div>
        <div><h3>Our Guarantee</h3><p>(If you're not satisfied with our work, we'll send an alternative cleaner to re-do it for free)</p></div>
      </li>
    </ul>
  </div>
</section>

<section class="steps">
  <h2 class="section-title"><span class="mark"></span>How It Works</h2>
  <div class="rule"></div>

  <div class="step" style="left:33px">
    <div class="step-ring"><div class="step-core"><svg viewBox="0 0 48 48"><path d="M42 6L6 22l14 6 6 14z"/><path d="M20 28L42 6"/></svg></div></div>
    <p>Select a service</p>
  </div>
  <div class="step-arrow" style="left:260px"><svg viewBox="0 0 90 30"><path d="M4 22Q45 0 84 20M74 12l10 8-12 4"/></svg></div>

  <div class="step" style="left:308px">
    <div class="step-ring"><div class="step-core"><svg viewBox="0 0 48 48"><circle cx="28" cy="27" r="14"/><path d="M28 18v9l6 4M24 9h8M4 20h10M2 27h10M6 34h8"/></svg></div></div>
    <p>Select A time &amp; date you'd<br>like a our professional to attend</p>
  </div>
  <div class="step-arrow" style="left:540px"><svg viewBox="0 0 90 30"><path d="M4 22Q45 0 84 20M74 12l10 8-12 4"/></svg></div>

  <div class="step" style="left:600px">
    <div class="step-ring"><div class="step-core soft"><svg viewBox="0 0 48 48" style="fill:#fff;stroke:none"><path d="M16 20v-6a8 8 0 0 1 16 0h-4a4 4 0 0 0-8 0v6z"/><rect x="10" y="20" width="28" height="22" rx="2"/></svg></div></div>
    <p>Pay securely online</p>
  </div>
  <div class="step-arrow" style="left:825px"><svg viewBox="0 0 90 30"><path d="M4 22Q45 0 84 20M74 12l10 8-12 4"/></svg></div>

  <div class="step" style="left:874px">
    <div class="step-ring"><div class="step-core"><svg viewBox="0 0 48 48"><circle cx="24" cy="24" r="19"/><circle cx="17" cy="19" r="1.5"/><circle cx="31" cy="19" r="1.5"/><path d="M15 28q9 9 18 0"/></svg></div></div>
    <p>Sit back, Relax and wait for one<br>of our professionals</p>
  </div>
</section>

<section class="testimonials">
  <h2 class="section-title"><span class="mark"></span>Testimonials</h2>
  <div class="rule"></div>
  <ul class="quote-list">
    <li class="quote" style="left:96px">
      <blockquote>Lorem ipsum dolor sit amet, consectetur adipisicing elit, sed do eiusmod tempor incididunt ut labore et dolore magna aliqua Unde omnis, consequuntur.</blockquote>
      <div class="reviewer"><div class="avatar" role="img" aria-label="Customer portrait"></div><div><div class="reviewer-name">JOHN DOE</div><div class="stars">★★★<span class="off">☆☆</span></div></div></div>
    </li>
    <li class="quote" style="left:453px">
      <blockquote>Lorem ipsum dolor sit amet, consectetur adipisicing elit, sed do eiusmod tempor incididunt ut labore et dolore magna aliqua Unde omnis, consequuntur.</blockquote>
      <div class="reviewer"><div class="avatar dark" role="img" aria-label="Customer portrait"></div><div><div class="reviewer-name">JOHN DOE</div><div class="stars">★★★<span class="off">☆☆</span></div></div></div>
    </li>
    <li class="quote" style="left:810px">
      <blockquote>Lorem ipsum dolor sit amet, consectetur adipisicing elit, sed do eiusmod tempor incididunt ut labore et dolore magna aliqua Unde omnis, consequuntur.</blockquote>
      <div class="reviewer"><div class="avatar" role="img" aria-label="Customer portrait"></div><div><div class="reviewer-name">JOHN DOE</div><div class="stars">★★★<span class="off">☆☆</span></div></div></div>
    </li>
  </ul>
</section>

<footer class="site-footer">
  <div class="footer-brand">
    <div class="brand"><span class="brand-dot"></span>tidyhaven</div>
    <div class="social" aria-label="Social links"><span></span><span></span><span></span><span></span></div>
  </div>

  <div class="footer-col newsletter">
    <h4>Newsletter</h4>
    <p>Excepteur sint occaecat cupidatat non proident, sunt in culpa qui</p>
    <div class="field">Enter Name</div>
    <span class="btn-subscribe">SUBSCRIBE</span>
  </div>

  <div class="footer-col contact">
    <h4>Contact Us</h4>
    <address>Tidyhaven No 218 Larkfield Rd.<br>Hollowmere, KS 66120</address>
    <div class="contact-line"><svg viewBox="0 0 18 18"><path d="M4 2l3 4-2 2c1 2 3 4 5 5l2-2 4 3-2 3C8 17 1 10 2 4z"/></svg>Call Us 555.210.4836</div>
    <div class="contact-line"><svg viewBox="0 0 18 18"><rect x="2" y="4" width="14" height="10"/><path d="M2 4l7 6 7-6"/></svg>Email: info@tidyhaven.com</div>
  </div>

  <div class="footer-col quick-links">
    <h4>Quick Links</h4>
    <ul>
      <li>Stayloft Tasks</li>
      <li>Stayloft Management</li>
      <li>Domestic Cleaning</li>
      <li>Handyman</li>
      <li>About</li>
      <li>Contact</li>
    </ul>
  </div>

  <div class="footer-bar">2016 © Copyrights Tidyhaven.All Rights Reserved</div>
</footer>

</body>
</html>
```